Surgical Procedure Room Letterhead

PLEASE DO NOT MAKE YOUR LETTERHEAD SIMILAR TO THE ONE I AM INCLUDING IN MY UPLOADS

Hello! I need my logo used to make a very clean, professional, simple letterhead that has all the pertinent information in it:
Location: 4182 NW 38th Lane, Suite 500
Tamarac, FL 33967
Phone: 954-218-4650
Fax: 800-642-9082

Can you please put this all on a word document that is easily editable? I will include my practice letterhead as an example ONLY of how easy it should be to write below the letterhead. Please don't make this letterhead the same as the one I am including in this example. They are two separate businesses.

Target Market(s)

Insurance companies

Industry/Entity Type

medical

Requirements
Must have
• classiness, elegance, simplicity
Should not have
• Please don't make your letterhead the same as the one that I included in my uploads

```html
<!DOCTYPE html>
<html lang="en">
<head>
<meta charset="utf-8">
<title>Harborline Surgical Suites Letterhead</title>
<link rel="stylesheet" href="https://fonts.googleapis.com/css2?family=Arimo:wght@400&family=Source+Sans+3:wght@400;600&display=swap">
<style>
  :root {
    --backdrop: #ababab;
    --paper: #f6f3f4;
    --navy: #00305a;
    --gold: #d9b03c;
    --ink: #4a4a4a;
    --ink-soft: #5a5a5a;
    --white: #ffffff;
  }
  * { margin: 0; padding: 0; box-sizing: border-box; }
  html, body { width: 942px; height: 1200px; overflow: hidden; }
  body { background: var(--backdrop); position: relative; }
  .letterhead {
    position: absolute; left: 45px; top: 0;
    width: 852px; height: 1200px;
    background: var(--paper); overflow: hidden;
    font-family: "Arimo", Arial, sans-serif; color: var(--ink);
  }
  .brand-name {
    position: absolute; left: 60px; top: 88px;
    font-family: "Source Sans 3", Arial, sans-serif; font-weight: 600;
    font-size: 27px; line-height: 1; color: var(--navy); letter-spacing: 0.5px;
  }
  .salutation { position: absolute; left: 60px; top: 298px; font-size: 24px; color: var(--ink-soft); }
  .letter-body { position: absolute; left: 60px; top: 362px; width: 734px; }
  .letter-body p {
    font-size: 13.2px; line-height: 20.5px; text-align: justify;
    color: var(--ink); margin-bottom: 20.5px;
  }
  .closing { position: absolute; left: 60px; top: 796px; font-size: 13.2px; }
  .signature-area {
    position: absolute; left: 67px; top: 880px; width: 112px; height: 30px;
    background: linear-gradient(180deg, rgba(30,35,50,0) 0%, rgba(30,35,50,0.12) 50%, rgba(30,35,50,0) 100%);
  }
  .signer-name { position: absolute; left: 73px; top: 940px; font-size: 19px; color: var(--ink-soft); }
  .signer-title { position: absolute; left: 73px; top: 968px; font-size: 15px; color: var(--ink-soft); }
  .footer-band { position: absolute; left: 0; top: 900px; width: 852px; height: 300px; }
  .contact {
    position: absolute; right: 53px; top: 1050px; text-align: right;
    font-family: "Source Sans 3", Arial, sans-serif; font-size: 14.5px;
    line-height: 18.5px; color: var(--white);
  }
  .contact-address { margin-bottom: 8px; }
  .contact-line { display: flex; justify-content: flex-end; align-items: center; gap: 8px; height: 20px; }
  .contact-icon { width: 13px; height: 13px; fill: var(--gold); }
</style>
</head>
<body>
  <main class="letterhead">
    <header class="brand-name">Harborline Surgical Suites</header>

    <p class="salutation">Dear Mr. Harlow,</p>

    <section class="letter-body">
      <p>Lorem ipsum dolor sit amet, consectetur adipiscing elit. Donec orci purus, luctus vitae dignissim eu, iaculis sed purus. Vivamus faucibus, ipsum nec aliquet viverra, leo mauris condimentum ligula, sit amet sagittis enim ligula quis arcu. Nam egestas tortor id nisi porttitor mattis. In tortor ante, ultricies in suscipit a, tempus non massa. Vivamus et auctor mi. Fusce vel massa nulla. Phasellus nec eros mauris, et scelerisque orci.</p>
      <p>Donec malesuada orci vitae nulla accumsan porta a id massa. Quisque accumsan iaculis magna sit amet fringilla. Maecenas consequat, magna eget tincidunt semper, odio nibh rutrum mi, id feugiat ante nisi eu risus. Vestibulum nunc orci, rhoncus a placerat in, ultricies in mi. Cras mattis varius eros, vel fringilla nisi suscipit eget. Quisque scelerisque sagittis nulla at porttitor.</p>
      <p>Sed id augue vitae urna euismod commodo aliquet a quam. Pellentesque arcu velit, cursus et malesuada ut, consequat et diam. Nullam erat sem, rhoncus id ullamcorper vitae, rhoncus et arcu. In ultricies ultricies nulla, ut rutrum nisi iaculis at. Donec eu magna a metus ornare faucibus. Fusce aliquet faucibus ultricies. Morbi semper, est id tincidunt gravida, sem arcu adipiscing lacus, ac bibendum nulla leo eu purus. Quisque nec diam sed risus consectetur a ccumsan quis quis nibh. Vestibulum id purus lorem.</p>
      <p>It is a long established fact that a reader will be distracted by the readable content of a page when looking at its layout. The point of using Lorem Ipsum is that it has a more-or-less normal distribution of letters, as opposed to using 'Content here, content here', making it look like readable English. Many desktop publishing packages</p>
    </section>

    <p class="closing">Sincerely,</p>
    <div class="signature-area" role="img" aria-label="Handwritten signature"></div>
    <p class="signer-name">Daniel Harlow</p>
    <p class="signer-title">CEO/ Founder</p>

    <svg class="footer-band" viewBox="0 900 852 300" aria-hidden="true">
      <path fill="var(--navy)" d="M0 1160 C260 1150 520 1070 852 1000 L852 1200 L0 1200 Z"/>
      <path fill="none" stroke="var(--gold)" stroke-width="3" d="M0 1150 C260 1140 520 1060 852 990"/>
    </svg>

    <footer class="contact">
      <div class="contact-address">
        4182 NW 38th Lane<br>
        Suite 500<br>
        Tamarac, FL 33967
      </div>
      <div class="contact-line">
        <span>954-218-4650</span>
        <svg class="contact-icon" viewBox="0 0 24 24" aria-label="Phone"><path d="M6.6 10.8a15.1 15.1 0 0 0 6.6 6.6l2.2-2.2c.3-.3.7-.4 1-.2 1.1.4 2.3.6 3.6.6.6 0 1 .4 1 1V20c0 .6-.4 1-1 1C10.6 21 3 13.4 3 4c0-.6.4-1 1-1h3.5c.6 0 1 .4 1 1 0 1.3.2 2.5.6 3.6.1.3 0 .7-.2 1z"/></svg>
      </div>
      <div class="contact-line">
        <span>800-642-9082</span>
        <svg class="contact-icon" viewBox="0 0 24 24" aria-label="Fax"><path d="M6 3h12v5H6z M3 9h18v9h-3v-3H6v3H3z M7 16h10v5H7z"/></svg>
      </div>
    </footer>
  </main>
</body>
</html>
```